Lurna Beauty Mobile App Design

We need an app design for a new on-demand beauty service app called Lurna Beauty. We help customers find and book beauty services on-demand (within 48 hours) or into the future. We would like to see designs that are clean and include the logs colors with dark and light shades of grey.
Design should be clean and modern yet showcase that this is a beauty app. It should beautiful and artful as well.
One set of mockups are attached, another set exists.
Competitors include primwick.example or dovatrine.example
Key: You can change the mockups to be best suited for functionality and design. These are here for content only.
Updates
The designs so far look great! Can you please design the portfolio screen for me to see navigation and a registration page to see your idea of textbox and buttons.
Industry/Entity Type
It Service
Look and feel
Each slider illustrates characteristics of the customer's brand and the style your logo design should communicate.

```html
<!DOCTYPE html>
<html lang="en">
<head>
<meta charset="utf-8">
<title>Lurna Beauty – Menu</title>
<link rel="stylesheet" href="https://fonts.googleapis.com/css2?family=Source+Sans+3:wght@400;500&family=Arimo:wght@400;700&display=swap">
<style>
  :root {
    --white: #ffffff;
    --ink: #111111;
    --muted-ink: #8a8a8a;
    --pink-light: #d57db2;
    --pink-mid: #c4679c;
    --plum: #9a3c74;
    --plum-deep: #86306a;
    --lilac: #a45f9c;
    --chevron: rgba(120, 38, 88, 0.55);
    --rule: rgba(255, 255, 255, 0.28);
    --divider: rgba(225, 225, 225, 0.85);
    --soft-text: rgba(255, 255, 255, 0.62);
  }
  * { margin: 0; padding: 0; box-sizing: border-box; }
  html, body { width: 676px; height: 1200px; overflow: hidden; background: var(--white); }
  .screen { position: relative; width: 676px; height: 1200px; overflow: hidden; font-family: "Source Sans 3", sans-serif; }

  .status-bar { position: absolute; top: 0; left: 0; width: 676px; height: 42px; background: var(--white); color: var(--ink); font-family: "Arimo", sans-serif; font-size: 22px; }
  .status-bar .signal { position: absolute; left: 12px; top: 13px; }
  .status-bar .carrier { position: absolute; left: 92px; top: 9px; }
  .status-bar .wifi { position: absolute; left: 163px; top: 10px; }
  .status-bar .clock { position: absolute; left: 0; width: 676px; top: 8px; text-align: center; font-weight: 700; font-size: 23px; }
  .status-bar .bluetooth { position: absolute; left: 520px; top: 9px; }
  .status-bar .battery-level { position: absolute; left: 551px; top: 9px; }
  .status-bar .battery { position: absolute; left: 610px; top: 11px; }

  .app-header { position: absolute; top: 42px; left: 0; width: 676px; height: 93px; background: var(--white); }
  .app-header .menu-toggle { position: absolute; left: 21px; top: 29px; }
  .app-header .title { position: absolute; left: 0; width: 676px; top: 19px; text-align: center; font-size: 28px; color: var(--ink); }

  .drawer { position: absolute; top: 135px; left: 0; width: 676px; height: 1065px;
    background:
      radial-gradient(ellipse 260px 200px at 290px 80px, rgba(222,140,190,0.9), transparent 70%),
      radial-gradient(ellipse 200px 160px at 520px 220px, rgba(150,50,110,0.7), transparent 70%),
      radial-gradient(ellipse 220px 200px at 640px 420px, rgba(140,45,105,0.8), transparent 70%),
      radial-gradient(ellipse 240px 220px at 200px 470px, rgba(220,130,185,0.75), transparent 70%),
      radial-gradient(ellipse 200px 260px at 0px 820px, rgba(140,45,105,0.85), transparent 70%),
      radial-gradient(ellipse 300px 240px at 380px 760px, rgba(205,115,170,0.7), transparent 70%),
      radial-gradient(ellipse 260px 200px at 660px 1040px, rgba(135,45,105,0.85), transparent 70%),
      radial-gradient(ellipse 220px 180px at 60px 40px, rgba(165,95,155,0.85), transparent 70%),
      linear-gradient(160deg, var(--lilac) 0%, var(--pink-mid) 35%, var(--plum) 60%, var(--pink-mid) 80%, var(--plum-deep) 100%);
  }

  .profile { position: absolute; top: 0; left: 0; width: 676px; height: 164px; border-bottom: 1.5px solid var(--divider); }
  .profile .avatar { position: absolute; left: 34px; top: 49px; width: 84px; height: 84px; border-radius: 50%;
    background: radial-gradient(circle at 50% 45%, #d9a12c 0%, #b5561e 45%, #6e1710 80%, #2a0a08 100%); }
  .profile .name { position: absolute; left: 149px; top: 60px; font-size: 27px; color: var(--white); }
  .profile .description { position: absolute; left: 149px; top: 97px; font-size: 21px; color: var(--soft-text); }

  .menu { position: absolute; top: 164px; left: 17px; width: 560px; list-style: none; }
  .menu-item { position: relative; height: 93px; border-bottom: 1px solid var(--rule); }
  .menu-item:last-child { border-bottom: none; }
  .menu-item .label { position: absolute; left: 11px; top: 25px; font-size: 35px; color: var(--white); }
  .menu-item .chevron { position: absolute; right: 30px; top: 35px; }

  .logout { position: absolute; left: 51px; top: 925px; width: 475px; height: 99px; border: 3px solid var(--white); border-radius: 50px;
    font-family: "Arimo", sans-serif; font-size: 37px; color: var(--white); display: flex; align-items: center; justify-content: center; padding-bottom: 4px; }
</style>
</head>
<body>
<div class="screen">
  <div class="status-bar">
    <svg class="signal" width="76" height="14" viewBox="0 0 76 14" aria-hidden="true">
      <circle cx="7" cy="7" r="6" fill="#111"/><circle cx="22" cy="7" r="6" fill="#111"/><circle cx="37" cy="7" r="6" fill="#111"/>
      <circle cx="52" cy="7" r="5.3" fill="none" stroke="#111" stroke-width="1.3"/><circle cx="67" cy="7" r="5.3" fill="none" stroke="#111" stroke-width="1.3"/>
    </svg>
    <span class="carrier">KESTEL</span>
    <svg class="wifi" width="26" height="20" viewBox="0 0 26 20" aria-hidden="true" style="left:180px">
      <path d="M13 19 L8.5 14 A6.5 6.5 0 0 1 17.5 14 Z" fill="#111"/>
      <path d="M4.5 10 A12 12 0 0 1 21.5 10" fill="none" stroke="#111" stroke-width="3"/>
      <path d="M1 6 A17 17 0 0 1 25 6" fill="none" stroke="#111" stroke-width="3"/>
    </svg>
    <span class="clock">4:21 PM</span>
    <svg class="bluetooth" width="16" height="26" viewBox="0 0 16 26" aria-hidden="true">
      <path d="M2 7 L14 18 L8 24 L8 2 L14 8 L2 19" fill="none" stroke="#8a8a8a" stroke-width="2"/>
    </svg>
    <span class="battery-level">22%</span>
    <svg class="battery" width="54" height="22" viewBox="0 0 54 22" aria-hidden="true">
      <rect x="1" y="1" width="47" height="20" rx="3" fill="none" stroke="#111" stroke-width="1.6"/>
      <rect x="4" y="4" width="10" height="14" fill="#111"/>
      <rect x="49.5" y="7" width="3" height="8" rx="1" fill="#111"/>
    </svg>
  </div>

  <header class="app-header">
    <svg class="menu-toggle" width="47" height="26" viewBox="0 0 47 26" aria-label="Menu">
      <rect x="0" y="2" width="47" height="3" fill="#111"/><rect x="0" y="11" width="47" height="3" fill="#111"/><rect x="0" y="20" width="47" height="3" fill="#111"/>
    </svg>
    <h1 class="title" style="font-weight:400">John Smith</h1>
  </header>

  <nav class="drawer">
    <div class="profile">
      <div class="avatar" role="img" aria-label="Profile picture of the user"></div>
      <div class="name">John Smith</div>
      <div class="description">Description</div>
    </div>

    <ul class="menu">
      <li class="menu-item"><span class="label">New Service</span>
        <svg class="chevron" width="14" height="24" viewBox="0 0 14 24" aria-hidden="true"><path d="M2 2 L12 12 L2 22" fill="none" stroke="var(--chevron)" stroke-width="3"/></svg></li>
      <li class="menu-item"><span class="label">Setting</span>
        <svg class="chevron" width="14" height="24" viewBox="0 0 14 24" aria-hidden="true"><path d="M2 2 L12 12 L2 22" fill="none" stroke="var(--chevron)" stroke-width="3"/></svg></li>
      <li class="menu-item"><span class="label">Share</span>
        <svg class="chevron" width="14" height="24" viewBox="0 0 14 24" aria-hidden="true"><path d="M2 2 L12 12 L2 22" fill="none" stroke="var(--chevron)" stroke-width="3"/></svg></li>
      <li class="menu-item"><span class="label">Notification</span>
        <svg class="chevron" width="14" height="24" viewBox="0 0 14 24" aria-hidden="true"><path d="M2 2 L12 12 L2 22" fill="none" stroke="var(--chevron)" stroke-width="3"/></svg></li>
    </ul>

    <div class="logout">Logout</div>
  </nav>
</div>
</body>
</html>
```